Brevimor Inc. Website

We need a website design for a new company based in Montreal, Canada. Our company offers professional services in planning & scheduling for major construction projects in varying industries. The main colors to be used are black & red (same as in logo). The final design should convey professionalism, precision, and excellence. The following are examples of what the website layout could look like: https://www.valqorix.ca/, https://4796.ca/, https://dumelvo.ca/, https://www.quorbintal.com/en. Avoid using stock videos or photos with people in it.
Target Market(s)
Target audience are multi-national clients looking to hire a firm to manage their construction projects. Target market is Mining & Metals
Industry/Entity Type
Mining & Metalurgy, Hydroelectricity, Infrastructure
Number of Pages Required
1 page
Colors
Designer to choose colors to be used in the design.
Look and feel
Each slider illustrates characteristics of the customer's brand and the style your logo design should communicate.

```html
<!DOCTYPE html>
<html lang="en">
<head>
<meta charset="utf-8">
<title>Brevimor Inc.</title>
<link href="https://fonts.googleapis.com/css2?family=Poppins:wght@400;500;600&family=Raleway:wght@700;800&display=swap" rel="stylesheet">
<style>
:root{
  --red:#a30d1e;
  --red-dark:#8a0a18;
  --black:#111111;
  --footer:#161616;
  --white:#ffffff;
  --text:#444444;
  --muted:#777777;
}
*{margin:0;padding:0;box-sizing:border-box}
html,body{width:1200px;height:4133px;overflow:hidden}
body{position:relative;font-family:'Poppins',sans-serif;color:var(--text);background:var(--white)}
.abs{position:absolute}
h1,h2,h3{font-family:'Raleway',sans-serif;font-weight:800;color:var(--black)}

/* header */
.site-header{left:0;top:0;width:1200px;height:126px;background:var(--white);z-index:3}
.nav{top:54px;font-size:14px;font-weight:600;color:var(--black);letter-spacing:.2px;display:flex;gap:26px}
.nav-left{left:79px}
.nav-right{right:79px}
.brand-tab{left:480px;top:0;width:240px;height:157px;background:var(--white);clip-path:polygon(0 0,100% 0,100% 80%,90% 100%,10% 100%,0 80%);display:flex;align-items:center;justify-content:center;gap:10px;z-index:4}
.brand-mark{width:34px;height:34px;border-radius:50%;background:var(--red)}
.brand-name{font-family:'Poppins',sans-serif;font-weight:600;font-size:22px;color:var(--red);letter-spacing:1px}

/* hero */
.hero{left:0;top:126px;width:1200px;height:616px;background:linear-gradient(160deg,#6b6e73 0%,#3f4246 45%,#2a2c2f 70%,#4a4c50 100%)}
.hero-title{left:0;top:318px;width:1200px;text-align:center;font-family:'Raleway',sans-serif;font-weight:700;font-size:54px;color:var(--white);letter-spacing:1px}
.hero-sub{left:330px;top:388px;width:540px;text-align:center;font-size:20px;line-height:29px;color:var(--white)}
.btn{display:inline-flex;align-items:center;justify-content:center;background:var(--red);color:var(--white);font-size:14px;font-weight:600;border-radius:22px;letter-spacing:.3px}
.hero-btn{left:528px;top:468px;width:144px;height:42px}

/* about */
.about-arrow{left:146px;top:742px}
.about-bar{left:0;top:853px;width:118px;height:26px;background:var(--red)}
.about-title{left:144px;top:842px;font-size:41px}
.about-lead{left:144px;top:915px;width:434px;font-size:14px;line-height:26px;text-align:justify}
.about-watermark{left:420px;top:800px;width:360px;height:210px;display:flex;align-items:center;justify-content:center;gap:12px;opacity:.12}
.about-watermark .brand-mark{width:60px;height:60px}
.about-watermark span{font-weight:600;font-size:34px;color:var(--red)}
.about-text{left:621px;top:845px;width:435px;font-size:14px;line-height:26px;text-align:justify}
.about-text p+p{margin-top:8px}
.read-more{left:623px;top:1036px;font-size:14px;font-weight:500;color:var(--red);text-decoration:underline;display:flex;align-items:center;gap:8px}
.photo-dam{left:488px;top:1150px;width:568px;height:345px;background:linear-gradient(180deg,#5c8a92 0%,#3e7b83 40%,#1f6f78 70%,#1c5a66 100%)}
.photo-frame{left:144px;top:1040px;width:448px;height:337px;background:linear-gradient(135deg,#9bbad6 0%,#3b4f73 50%,#1f2a44 80%,#d98a3a 100%)}
.frame-line{background:var(--red)}

/* services */
.services-band{left:0;top:1631px;width:1200px;height:161px;background:var(--black)}
.services-title{left:144px;top:1684px;font-size:44px;color:var(--white)}
.services-divider{left:402px;top:1655px;width:3px;height:112px;background:var(--white)}
.services-intro{left:458px;top:1684px;width:598px;font-size:14px;line-height:25px;color:var(--white);text-align:justify}

.card-photo{top:1869px;height:335px}
.card-box{top:2137px;width:378px;height:137px;padding:24px 26px;box-shadow:0 6px 22px rgba(0,0,0,.12)}
.card-box h3{font-family:'Poppins',sans-serif;font-weight:600;font-size:18px;margin-bottom:10px}
.card-box p{font-size:14px;line-height:24px}
.card-light{left:80px;background:var(--white)}
.card-red{left:616px;background:var(--red)}
.card-red h3,.card-red p{color:var(--white)}

/* projects */
.projects-title{left:0;top:2393px;width:1200px;text-align:center;font-family:'Raleway',sans-serif;font-weight:700;font-size:41px;color:var(--black)}
.project{width:320px;height:280px}

/* callback */
.callback{left:0;top:3226px;width:1200px;height:579px;background:linear-gradient(180deg,#a8101f 0%,#9b0d1c 100%)}
.callback-title{left:127px;top:3302px;font-family:'Raleway',sans-serif;font-weight:800;font-size:34px;color:var(--white)}
.field{width:208px;border-bottom:1px solid rgba(255,255,255,.6);padding-bottom:8px;color:var(--white)}
.field label{display:block;font-size:13px;font-weight:600;letter-spacing:.3px}
.field span{display:block;font-size:13px;margin-top:4px}
.field-wide{width:448px}
.submit{left:128px;top:3676px;width:157px;height:48px;background:var(--black);color:var(--white);font-size:14px;font-weight:600;border-radius:24px;display:flex;align-items:center;justify-content:center}
.contact-card{left:656px;top:3310px;width:416px;height:415px;background:var(--white);text-align:center;padding:64px 38px 0}
.contact-card h2{font-family:'Raleway',sans-serif;font-weight:800;font-size:33px;margin-bottom:20px}
.contact-card p{font-size:14px;line-height:26px;color:var(--muted)}
.contact-card .btn{width:140px;height:48px;border-radius:24px;margin-top:30px}

/* footer */
.footer{left:0;top:3805px;width:1200px;height:328px;background:var(--footer);color:var(--white)}
.footer-brand{left:145px;top:3935px;display:flex;align-items:center;gap:12px}
.footer-brand .brand-mark{background:var(--white);width:40px;height:40px}
.footer-brand span{font-weight:600;font-size:24px;color:var(--white);letter-spacing:1px}
.footer-head{font-family:'Poppins',sans-serif;font-weight:600;font-size:17px;color:var(--white)}
.footer-head::after{content:"";display:block;width:60px;height:2px;background:var(--red);margin-top:6px}
.footer-links{font-size:12px;line-height:24px;color:#ddd;list-style:none}
.footer-contact{font-size:12px;color:#ddd;list-style:none}
.footer-contact li{display:flex;align-items:center;gap:14px;height:37px}
.subscribe-note{font-size:12px;line-height:19px;color:#ddd}
.subscribe-form{left:820px;top:3966px;width:236px;height:36px;background:var(--white);border-radius:18px;overflow:hidden;display:flex}
.subscribe-form span{flex:1;font-size:10px;color:#999;padding:11px 14px}
.subscribe-form i{width:44px;background:var(--red);display:flex;align-items:center;justify-content:center}
.footer-rule{left:0;top:4073px;width:1200px;height:1px;background:#2c2c2c}
.copyright{left:143px;top:4100px;font-size:13px;color:#ddd}
.copyright u{color:var(--white)}
.social{top:4094px;width:28px;height:28px;border-radius:50%}
</style>
</head>
<body>

<header class="abs site-header">
  <nav class="abs nav nav-left"><span>HOME</span><span>SERVICES</span><span>ABOUT US</span></nav>
  <nav class="abs nav nav-right"><span>GALLERY</span><span>CAREERS</span><span>CONTACT US</span></nav>
</header>
<div class="abs brand-tab"><span class="brand-mark"></span><span class="brand-name">BREVIMOR</span></div>

<section class="abs hero" role="img" aria-label="Aerial view of an open-pit mine with a yellow bucket-wheel excavator"></section>
<h1 class="abs hero-title">BREVIMOR INC</h1>
<p class="abs hero-sub">Lorem ipsum dolor sit amet, consectetur adipis cing elit, sed do eiusmod tempor.</p>
<a class="abs btn hero-btn">CONTACT US</a>

<svg class="abs about-arrow" width="10" height="90" viewBox="0 0 10 90"><line x1="5" y1="0" x2="5" y2="86" stroke="#a30d1e" stroke-width="1.5"/><polyline points="1,80 5,87 9,80" fill="none" stroke="#a30d1e" stroke-width="1.5"/></svg>
<div class="abs about-bar"></div>
<h2 class="abs about-title">ABOUT US</h2>
<p class="abs about-lead">Lorem ipsum dolor sit amet, consectetur adipiscing elit, sed do eiusmod tempor incididunt ut labore et dolore magna aliqua. Ut enim ad minim veniam.</p>
<div class="abs about-watermark" aria-hidden="true"><span class="brand-mark"></span><span>BREVIMOR</span></div>
<div class="abs about-text">
  <p>Lorem ipsum dolor sit amet, consectetur adipiscing elit, sed do eiusmod tempor incididunt ut labore et dolore magna aliqua. Ut enim ad minim veniam, quis nostrud exercitation ullamco laboris nisi ut aliquip.</p>
  <p>Lorem ipsum dolor sit amet, consectetur adipiscing elit, sed do eiusmod tempor incididunt.</p>
</div>
<a class="abs read-more">Read More <svg width="12" height="12" viewBox="0 0 12 12"><path d="M1 6h9M6 2l4 4-4 4" stroke="#a30d1e" stroke-width="2" fill="none"/></svg></a>

<div class="abs frame-line" style="left:592px;top:1092px;width:182px;height:5px"></div>
<div class="abs frame-line" style="left:769px;top:1092px;width:5px;height:60px"></div>
<div class="abs frame-line" style="left:365px;top:1375px;width:5px;height:66px"></div>
<div class="abs frame-line" style="left:365px;top:1436px;width:125px;height:5px"></div>
<div class="abs photo-dam" role="img" aria-label="Hydroelectric dam in a green mountain valley with turquoise water"></div>
<div class="abs photo-frame" role="img" aria-label="Steel building frame under construction with a tower crane at sunset"></div>

<section class="abs services-band"></section>
<h2 class="abs services-title">SERVICES</h2>
<div class="abs services-divider"></div>
<p class="abs services-intro">Lorem ipsum dolor sit amet, consectetur adipiscing elit, sed do eiusmod tempor incididunt ut labore et dolore magna aliqua.</p>

<div class="abs card-photo" style="left:80px;width:504px;background:linear-gradient(135deg,#e0b83a 0%,#b6a98a 40%,#cfcac0 70%,#8d8a84 100%)" role="img" aria-label="Blueprints, tools and hard hats on a planning table"></div>
<div class="abs card-box card-light"><h3>PLANNING</h3><p>Lorem ipsum dolor sit amet, consectetur adi piscing elit, sed do eiusm.</p></div>

<div class="abs" style="left:616px;top:1869px;width:24px;height:405px;background:var(--red)"></div>
<div class="abs card-photo" style="left:640px;width:480px;background:linear-gradient(180deg,#7d9aa6 0%,#3d6b4a 40%,#27b3b8 65%,#2d5a3a 100%)" role="img" aria-label="Turquoise reservoir lake between forested mountains"></div>
<div class="abs card-box card-red"><h3>SCHEDULING</h3><p>Lorem ipsum dolor sit amet, consectetur adi piscing elit, sed do eiusm.</p></div>

<h2 class="abs projects-title">CONSTRUCTION PROJECTS</h2>
<div class="abs project" style="left:80px;top:2500px;background:linear-gradient(160deg,#7fa8b8 0%,#6e8b4a 45%,#8a7a62 70%,#4f7a3c 100%)" role="img" aria-label="Aerial view of a hydroelectric spillway"></div>
<div class="abs project" style="left:440px;top:2500px;background:linear-gradient(160deg,#a9b8c4 0%,#5e7182 45%,#3d4a55 100%)" role="img" aria-label="Open-pit mine with haul trucks"></div>
<div class="abs project" style="left:800px;top:2500px;background:linear-gradient(180deg,#8fb0cf 0%,#c8b89a 50%,#6a6f7a 100%)" role="img" aria-label="Tower cranes over a building site at sunset"></div>
<div class="abs project" style="left:80px;top:2820px;background:linear-gradient(180deg,#2d4a7a 0%,#5a5a4a 55%,#c88a2e 80%,#2a2a2a 100%)" role="img" aria-label="Illuminated industrial conveyor plant at dusk"></div>
<div class="abs project" style="left:440px;top:2820px;background:radial-gradient(circle at 50% 50%,#9cc0dc 0%,#b88c5a 40%,#7a7a7a 62%,#c9c9c9 100%)" role="img" aria-label="Pipeline trench seen through a large pipe section"></div>
<div class="abs project" style="left:800px;top:2820px;background:linear-gradient(180deg,#8aa2b0 0%,#3e5a4a 40%,#6f8fa0 65%,#2c3f4a 100%)" role="img" aria-label="Dam across a river between hills"></div>

<section class="abs callback" role="img" aria-label="Red-tinted aerial background of a mining site"></section>
<h2 class="abs callback-title">REQUEST A CALL BACK</h2>
<div class="abs field" style="left:128px;top:3392px"><label>FIRST NAME</label><span>John</span></div>
<div class="abs field" style="left:367px;top:3392px"><label>LAST NAME</label><span>Doe</span></div>
<div class="abs field" style="left:128px;top:3467px"><label>EMAIL ADDRESS</label><span>johndoe@mailvero.com</span></div>
<div class="abs field" style="left:367px;top:3467px"><label>PHONE</label><span>+123 456 7890</span></div>
<div class="abs field field-wide" style="left:128px;top:3542px"><label>MESSAGE</label><span style="margin-top:54px">Enter your message</span></div>
<a class="abs submit">SUBMIT</a>
<div class="abs contact-card">
  <h2>CONTACT US</h2>
  <p>Lorem ipsum dolor sit amet, consectetur adipis cing elit, sed do eiusmod tempor incididunt ut labore et dolore magna aliqua. Ut enim ad minim veniam, quis nostrud.</p>
  <a class="btn">CONTACT US</a>
</div>

<footer class="abs footer"></footer>
<div class="abs footer-brand"><span class="brand-mark"></span><span>BREVIMOR</span></div>

<h3 class="abs footer-head" style="left:385px;top:3858px">QUICK LINKS</h3>
<ul class="abs footer-links" style="left:390px;top:3910px">
  <li>Home</li><li>Services</li><li>About Us</li><li>Gallery</li><li>Careers</li><li>Contact Us</li>
</ul>

<h3 class="abs footer-head" style="left:565px;top:3858px">CONTACT US</h3>
<ul class="abs footer-contact" style="left:568px;top:3910px">
  <li><svg width="12" height="12" viewBox="0 0 24 24"><path fill="#fff" d="M6.6 10.8a15 15 0 0 0 6.6 6.6l2.2-2.2c.3-.3.7-.4 1-.2 1.1.4 2.3.6 3.6.6.6 0 1 .4 1 1V20c0 .6-.4 1-1 1A17 17 0 0 1 3 4c0-.6.4-1 1-1h3.5c.6 0 1 .4 1 1 0 1.3.2 2.5.6 3.6.1.3 0 .7-.2 1z"/></svg>123 456 7890</li>
  <li><svg width="12" height="10" viewBox="0 0 24 18"><rect x="1" y="1" width="22" height="16" rx="2" fill="#fff"/><path d="M1 2l11 8 11-8" stroke="#161616" stroke-width="2" fill="none"/></svg>info@companyname.com</li>
  <li><svg width="10" height="13" viewBox="0 0 20 26"><path fill="#fff" d="M10 0a9 9 0 0 0-9 9c0 7 9 17 9 17s9-10 9-17a9 9 0 0 0-9-9zm0 12a3 3 0 1 1 0-6 3 3 0 0 1 0 6z"/></svg>Company address</li>
</ul>

<h3 class="abs footer-head" style="left:815px;top:3858px">SUBSCRIBE</h3>
<p class="abs subscribe-note" style="left:820px;top:3912px;width:240px">Sign up today to get resources on how to attract and retain more customers!</p>
<div class="abs subscribe-form"><span>✉ Email Address</span><i><svg width="14" height="14" viewBox="0 0 24 24"><path fill="#fff" d="M2 12l20-9-6 19-4-7z"/></svg></i></div>

<div class="abs footer-rule"></div>
<p class="abs copyright">Copyright© 2023 <u>Company name</u> | All Rights Reserved</p>
<span class="abs social" style="left:956px;background:var(--white)"></span>
<span class="abs social" style="left:992px;background:var(--red)"></span>
<span class="abs social" style="left:1028px;background:var(--white)"></span>

</body>
</html>
```